Website Design for Solar Panel Company

We are working with a company called BrightVX.

Some sites to use for content/competitors and inspiration:
https://www.dawnmill.com
https://prod.cdn-prod.raylokt.com
https://mossbeamvolt.net
https://www.quorvin.com/solarpanels

Thank you for taking the time to consider designing a website for us. We are web developers based in Stockton, CA, USA. Most of our projects go through the same process. Understanding this process may help you win a project with us. We custom-code all of our websites in-house. We don’t have any requirements as to what tools you use for your design, but we prefer Figma files. For any design that we label as four-stars, we send it to the client for review. The client picks the final design they want us to use. Once we complete this process, we will continue to show additional clients all the four-star sites and purchase them later. Your designs will have multiple chances to sell. For better chances of success, we ask that you follow these guidelines.

IMAGES:
If you use any images or icons in the design, we ask that you have a link to the asset so we can purchase the image/icon. Most of the designs we submit do not have the customer’s images on them unless they have some great images. Be creative; show us the feeling you are trying to portray with your image choices. Use any royalty-free site you choose. We subscribe to Corvane and mainly use their images, but we can purchase images outside of Corvane. PLEASE NOTE: we will not submit designs to clients with watermarks on the images.

FONTS:
We ask that you identify the fonts used in the design. This can be done in a message if you want. We typically use Tivelo Fonts and Corvane Fonts.

CONTENT:
We're always open to different content and ideas. We often submit designs with stock images so the client can see our vision. We typically take pictures after the website launch to use their images with our vision. Lorem Ipsum is fine for paragraphs, but we ask that you write the headers in correct English. We want to be able to show the vision and identify the sections of the website.

INSPIRATION:
We typically add a couple of links in the brief of websites we like to help you get started in your design.

REVISIONS:
We do not often ask for revisions of the designs unless we see something in the design that may not appeal to the client. If there are slight changes that we want to make, we do that in the development process.

FEEDBACK:
We rarely give feedback on designs during the design process. We are working on many website projects and do not have the time to provide feedback. We usually respond if your request is well thought out and asks specific questions, but a note asking “feedback, please” usually goes unanswered.

```html
<!DOCTYPE html>
<html lang="en">
<head>
<meta charset="utf-8">
<title>BrightVX — Solar Energy</title>
<link rel="stylesheet" href="https://fonts.googleapis.com/css2?family=Poppins:wght@400;500;600;700&family=Roboto:ital,wght@0,400;0,500;1,400&display=swap">
<style>
:root{
  --green:#5ccf25;
  --green-dark:#2f9a12;
  --green-light:#74e033;
  --black:#0b0b0b;
  --ink:#111;
  --grey:#6b6b6b;
  --field:#f5f5f5;
  --white:#fff;
  --muted:#2a2a2a;
}
*{margin:0;padding:0;box-sizing:border-box}
html,body{width:1200px;height:5134px;overflow:hidden}
body{font-family:"Poppins",sans-serif;color:var(--ink);background:var(--white);position:relative}
.abs{position:absolute}
.brand{font-family:"Poppins",sans-serif;font-weight:700;font-size:40px;color:var(--ink);display:flex;align-items:center;gap:10px;letter-spacing:-0.5px}
.brand .dot{width:22px;height:22px;border-radius:50%;background:var(--green)}
.site-header{top:0;left:0;width:1200px;height:96px}
.contact-item{display:flex;align-items:center;gap:22px;top:20px}
.contact-icon{width:56px;height:56px;border-radius:50%;background:var(--black);display:flex;align-items:center;justify-content:center}
.contact-label{color:var(--green);font-size:18px;line-height:20px}
.contact-value{color:var(--grey);font-size:15px;line-height:20px}
.btn{display:flex;align-items:center;justify-content:center;font-weight:500;color:var(--white);text-decoration:none;border-radius:8px}
.btn-black{background:var(--black)}
.btn-green{background:linear-gradient(90deg,var(--green-dark),var(--green-light))}
.main-nav{top:96px;left:0;width:1200px;height:56px;background:var(--green);display:flex;justify-content:center;align-items:center;gap:0}
.main-nav a{color:var(--white);text-decoration:none;font-size:18px;font-weight:500;margin:0 27px}
.hero{top:152px;left:0;width:1200px;height:630px;background:linear-gradient(180deg,#6f8aa3 0%,#3b4b58 38%,#2e3a2a 62%,#3f5a22 100%)}
.hero-title{top:152px;width:1200px;text-align:center;color:var(--white);font-size:56px;font-weight:700;letter-spacing:0.5px}
.hero-text{top:242px;left:300px;width:600px;text-align:center;color:var(--white);font-size:16px;line-height:22px}
.section-title{font-size:40px;font-weight:700;color:var(--ink);line-height:1}
.rule{height:4px;background:var(--green);border-radius:2px}
.para{font-size:13px;line-height:18px;color:var(--grey)}
.round-photo{border-radius:50%}
.feature{width:300px;text-align:center;font-size:21px;line-height:28px;color:var(--ink)}
.feature svg{display:block;margin:0 auto 14px}
.dark-panel{background:var(--black)}
.dark-title{color:var(--white);font-size:40px;font-weight:600;line-height:1}
.ghost{color:var(--muted);font-size:26px;font-weight:700;line-height:1}
.dark-text{color:#d8d8d8;font-size:11.5px;line-height:15px}
.checklist{list-style:none}
.checklist li{display:flex;align-items:center;gap:10px;color:#e6e6e6;font-size:13px;height:42px}
.btn-small{font-size:12px;font-weight:600;border-radius:3px;height:32px;width:136px;background:var(--green)}
.field{background:var(--field);border-radius:4px;color:#555;font-size:19px;padding:0 24px;display:flex;align-items:center}
.submit{background:linear-gradient(90deg,#2b9210,#72e230);color:var(--white);font-size:19px;font-weight:600;display:flex;align-items:center;justify-content:center}
.blog-title{width:1200px;text-align:center;font-size:38px;font-weight:600}
.blog-card{width:212px}
.blog-card .thumb{width:212px;height:250px}
.blog-card p{margin-top:18px;font-family:"Roboto",sans-serif;font-size:14px;line-height:26px;color:#333;text-decoration:underline;padding-left:10px}
.quote{width:420px;font-family:"Roboto",sans-serif;font-style:italic;font-size:15.5px;line-height:30px;color:#8a8a8a}
.person{display:flex;align-items:center;gap:24px}
.avatar{width:68px;height:68px;border-radius:50%;background:linear-gradient(135deg,#c9b7a6,#7a6a5c)}
.person-name{font-size:22px;font-weight:500;color:#777;line-height:26px}
.person-role{font-size:18px;color:var(--green-dark);line-height:24px}
.dots{display:flex;gap:22px}
.dots span{width:16px;height:16px;border-radius:50%;background:#888}
.dots span.active{background:var(--green-dark)}
.site-footer{top:4700px;left:0;width:1200px;height:434px;background:var(--black);color:var(--white)}
.footer-heading{font-size:21px;font-weight:400;color:var(--white)}
.footer-list{list-style:none}
.footer-list li{display:flex;align-items:center;gap:16px;font-size:14px;color:#e6e6e6;height:45px}
.hours li{height:53px}
.social{display:flex;gap:30px}
.social span{width:18px;height:18px;border-radius:50%;background:var(--white)}
.email-field{width:180px;height:36px;background:var(--white);color:#999;font-size:11px;display:flex;align-items:center;justify-content:center;letter-spacing:0.5px}
.legal{font-size:11px;color:#ddd}
</style>
</head>
<body>

<!-- Header -->
<header class="abs site-header">
  <div class="abs brand" style="top:20px;left:66px;"><span class="dot"></span>BrightVX</div>
  <div class="abs contact-item" style="left:428px;">
    <div class="contact-icon">
      <svg width="26" height="26" viewBox="0 0 24 24"><path fill="#fff" d="M6.6 10.8a15.1 15.1 0 0 0 6.6 6.6l2.2-2.2c.3-.3.7-.4 1-.2 1.1.4 2.3.6 3.6.6.6 0 1 .4 1 1V20c0 .6-.4 1-1 1A17 17 0 0 1 3 4c0-.6.4-1 1-1h3.5c.6 0 1 .4 1 1 0 1.3.2 2.5.6 3.6.1.3 0 .7-.2 1z"/></svg>
    </div>
    <div><div class="contact-label">CALL US</div><div class="contact-value">888 888 8888</div></div>
  </div>
  <div class="abs contact-item" style="left:676px;">
    <div class="contact-icon">
      <svg width="26" height="26" viewBox="0 0 24 24"><rect x="3" y="6" width="18" height="12" rx="1.5" fill="#fff"/><path d="M3.5 6.5 12 13l8.5-6.5" stroke="#0b0b0b" stroke-width="1.6" fill="none"/></svg>
    </div>
    <div><div class="contact-label">EMAIL US</div><div class="contact-value">info@domain.com</div></div>
  </div>
  <a class="abs btn btn-black" style="top:28px;left:964px;width:186px;height:44px;font-size:18px;border-radius:8px;" href="#">GET A QUOTE</a>
</header>

<nav class="abs main-nav">
  <a href="#">HOME</a><a href="#">ABOUT US</a><a href="#">SERVICES</a><a href="#">PRICES</a><a href="#">FAQS</a><a href="#">CONTACT</a>
</nav>

<!-- Hero -->
<section class="abs hero" role="img" aria-label="Photo of large solar panel arrays standing in a green field under a cloudy sky">
  <h1 class="abs hero-title" style="top:152px;">BRIGHTVX</h1>
  <p class="abs hero-text">Lorem ipsum dolor sit amet, consectetur adipiscing elit, sed do eiusmod tempor incididunt ut labore et dolore magna aliqua.</p>
  <a class="abs btn btn-black" style="top:326px;left:396px;width:184px;height:44px;font-size:19px;" href="#">GET A QUOTE</a>
  <a class="abs btn btn-green" style="top:324px;left:606px;width:186px;height:44px;font-size:19px;" href="#">OUR PRODUCTS</a>
</section>

<!-- About -->
<section>
  <div class="abs round-photo" style="top:906px;left:76px;width:402px;height:402px;background:radial-gradient(circle at 50% 35%,#eef4f8 0%,#9fc1d6 40%,#5d7f3a 70%,#2f4d5e 100%);" role="img" aria-label="Photo of a tree above solar panels against a bright sky"></div>
  <h2 class="abs section-title" style="top:976px;left:586px;">ABOUT US</h2>
  <div class="abs rule" style="top:1020px;left:588px;width:116px;"></div>
  <p class="abs para" style="top:1034px;left:586px;width:560px;">Lorem ipsum dolor sit amet, consectetur adipiscing elit, sed do eiusmod tempor incididunt ut labore et doloremagna aliqua. Ut enim ad minim veniam, quis nostrud exercitation ullamco laboris nisi ut aliquip ex ea commodo consequat. Duis aute irure dolor in reprehenderit in voluptate velit esse cillum dolore eu fugiat nulla pariatur.</p>
  <p class="abs para" style="top:1124px;left:586px;width:560px;">Excepteur sint occaecat cupidatat non proident, sunt in culpa qui officia deserunt mollit anim id est laborum.</p>
  <a class="abs btn btn-green" style="top:1190px;left:588px;width:188px;height:46px;font-size:19px;" href="#">GET A QUOTE</a>
</section>

<!-- Features -->
<section>
  <div class="abs feature" style="top:1386px;left:134px;">
    <svg width="84" height="84" viewBox="0 0 84 84" fill="none" stroke="#3bb21c" stroke-width="2.5"><circle cx="36" cy="40" r="18"/><path d="M40 32c-2-2-8-2-8 2s8 2 8 6-6 4-8 2M36 28v24"/><path d="M50 16l14 4-4 14M8 60l18 10 24-6 20-14"/></svg>
    Guaranteed Lowest<br>Price
  </div>
  <div class="abs feature" style="top:1362px;left:460px;">
    <svg width="90" height="96" viewBox="0 0 90 96" fill="none" stroke="#3bb21c" stroke-width="2.5"><circle cx="45" cy="14" r="7"/><path d="M45 0v3M33 14h-4M61 14h-4M36 5l2 2M54 5l-2 2"/><path d="M20 36h50l8 22H12z"/><path d="M16 47h58M37 36l-3 22M53 36l3 22M45 58v14"/><path d="M10 88c10-10 20-14 35-14s25 4 35 14"/></svg>
    Integrated<br>Product Ecosystem
  </div>
  <div class="abs feature" style="top:1376px;left:780px;">
    <svg width="84" height="88" viewBox="0 0 84 88" fill="none" stroke="#3bb21c" stroke-width="2.5"><rect x="18" y="4" width="34" height="64" rx="5"/><path d="M30 10h10"/><circle cx="46" cy="46" r="13"/><path d="M55 55l16 16"/></svg>
    System Performance<br>Monitoring
  </div>
</section>

<!-- Save your money -->
<section>
  <div class="abs" style="top:1604px;left:0;width:610px;height:500px;background:linear-gradient(160deg,#a9c3d6 0%,#6e8b5a 30%,#4a5663 55%,#d7dadb 100%);" role="img" aria-label="Photo of a house roof covered with solar panels in a valley"></div>
  <div class="abs dark-panel" style="top:1604px;left:610px;width:590px;height:500px;"></div>
  <h2 class="abs dark-title" style="top:1676px;left:668px;">SAVE YOUR MONEY</h2>
  <div class="abs ghost" style="top:1726px;left:680px;">BRIGHTVX</div>
  <p class="abs dark-text" style="top:1776px;left:682px;width:470px;">Excepteur sint occaecat cupidatat non proident, sunt in culpa qui officia deserunt mollit anim id est laborum.</p>
  <ul class="abs checklist" style="top:1822px;left:682px;">
    <li><svg width="18" height="18" viewBox="0 0 18 18" fill="none" stroke="#5ccf25" stroke-width="2"><path d="M5 4a7 7 0 1 0 8 0M9 1v8"/></svg>Improve your family lifestyle</li>
    <li><svg width="18" height="18" viewBox="0 0 18 18" fill="none" stroke="#5ccf25" stroke-width="2"><path d="M5 4a7 7 0 1 0 8 0M9 1v8"/></svg>Lower your current power bills</li>
    <li><svg width="18" height="18" viewBox="0 0 18 18" fill="none" stroke="#5ccf25" stroke-width="2"><path d="M5 4a7 7 0 1 0 8 0M9 1v8"/></svg>Upgrade your usable space</li>
  </ul>
  <a class="abs btn btn-small" style="top:1962px;left:680px;" href="#">GET A QUOTE</a>
</section>

<!-- Order and installation -->
<section>
  <h2 class="abs section-title" style="top:2268px;left:94px;">ORDER AND INSTALLATION</h2>
  <div class="abs rule" style="top:2328px;left:96px;width:116px;"></div>
  <p class="abs para" style="top:2348px;left:96px;width:560px;">Lorem ipsum dolor sit amet, consectetur adipiscing elit, sed do eiusmod tempor incididunt ut labore et doloremagna aliqua. Ut enim ad minim veniam, quis nostrud exercitation ullamco laboris nisi ut aliquip ex ea commodo consequat. Duis aute irure dolor in reprehenderit in voluptate velit esse cillum dolore eu fugiat nulla pariatur.</p>
  <p class="abs para" style="top:2438px;left:96px;width:560px;">Excepteur sint occaecat cupidatat non proident, sunt in culpa qui officia deserunt mollit anim id est laborum.</p>
  <a class="abs btn btn-green" style="top:2504px;left:98px;width:188px;height:46px;font-size:19px;" href="#">GET A QUOTE</a>
  <div class="abs round-photo" style="top:2200px;left:730px;width:402px;height:402px;background:radial-gradient(circle at 40% 30%,#e9f7ff 0%,#4aa8d8 45%,#1f6e9e 70%,#4f8f2a 100%);" role="img" aria-label="Illustration of a robot carrying a solar panel through a flower meadow"></div>
</section>

<!-- Quote form -->
<form>
  <div class="abs field" style="top:2720px;left:146px;width:434px;height:56px;">Your Name</div>
  <div class="abs field" style="top:2720px;left:626px;width:432px;height:56px;">Your Phone</div>
  <div class="abs field" style="top:2810px;left:146px;width:434px;height:56px;">Email Address</div>
  <div class="abs field" style="top:2810px;left:626px;width:432px;height:56px;">Select Service</div>
  <div class="abs field" style="top:2898px;left:146px;width:912px;height:114px;align-items:flex-start;padding-top:20px;">Additional Message</div>
  <div class="abs submit" style="top:3046px;left:142px;width:912px;height:70px;">GET A FREE QUOTE NOW</div>
</form>

<!-- Monitoring -->
<section>
  <div class="abs dark-panel" style="top:3194px;left:0;width:1200px;height:552px;"></div>
  <div class="abs" style="top:3242px;left:118px;width:186px;height:392px;border-radius:18px;background:linear-gradient(180deg,#1a2346 0%,#3b2b7a 45%,#141a33 100%);" role="img" aria-label="Phone screen showing a solar monitoring app chart"></div>
  <div class="abs" style="top:3242px;left:342px;width:186px;height:392px;border-radius:18px;background:linear-gradient(180deg,#1b2547 0%,#2b3a6e 50%,#1a2240 100%);" role="img" aria-label="Phone screen showing a solar energy dashboard"></div>
  <h2 class="abs dark-title" style="top:3266px;left:676px;">24/7 MONITORING</h2>
  <div class="abs ghost" style="top:3316px;left:680px;">BRIGHTVX</div>
  <p class="abs dark-text" style="top:3366px;left:682px;width:470px;">Excepteur sint occaecat cupidatat non proident, sunt in culpa qui officia deserunt mollit anim id est laborum.</p>
  <ul class="abs checklist" style="top:3412px;left:682px;">
    <li><svg width="18" height="18" viewBox="0 0 18 18" fill="none" stroke="#5ccf25" stroke-width="2"><path d="M5 4a7 7 0 1 0 8 0M9 1v8"/></svg>Improve your family lifestyle</li>
    <li><svg width="18" height="18" viewBox="0 0 18 18" fill="none" stroke="#5ccf25" stroke-width="2"><path d="M5 4a7 7 0 1 0 8 0M9 1v8"/></svg>Lower your current power bills</li>
    <li><svg width="18" height="18" viewBox="0 0 18 18" fill="none" stroke="#5ccf25" stroke-width="2"><path d="M5 4a7 7 0 1 0 8 0M9 1v8"/></svg>Upgrade your usable space</li>
  </ul>
  <a class="abs btn btn-small" style="top:3552px;left:680px;" href="#">GET A QUOTE</a>
</section>

<!-- Blog -->
<section>
  <h2 class="abs blog-title" style="top:3762px;left:0;">RECENT FROM BLOG</h2>
  <div class="abs rule" style="top:3808px;left:530px;width:130px;"></div>
  <article class="abs blog-card" style="top:3880px;left:76px;">
    <div class="thumb" style="background:linear-gradient(180deg,#5fb6e6,#9dd3ef 60%,#4c8f2c);" role="img" aria-label="Illustration of a robot carrying a solar panel"></div>
    <p>Lorem ipsum dolor sit amet, consectetur adipiscing elit.</p>
  </article>
  <article class="abs blog-card" style="top:3880px;left:352px;">
    <div class="thumb" style="background:linear-gradient(160deg,#8fa0a8,#4c5660 50%,#c7cbcc);" role="img" aria-label="Photo of a roof with solar panels"></div>
    <p>Lorem ipsum dolor sit amet, consectetur adipiscing elit.</p>
  </article>
  <article class="abs blog-card" style="top:3880px;left:628px;">
    <div class="thumb" style="background:linear-gradient(180deg,#9fb6c8,#3c4d63 50%,#c8a070);" role="img" aria-label="Photo of installers working on solar panels"></div>
    <p>Lorem ipsum dolor sit amet, consectetur adipiscing elit.</p>
  </article>
  <article class="abs blog-card" style="top:3880px;left:904px;">
    <div class="thumb" style="background:linear-gradient(180deg,#8ec3ec,#cfe6f7 55%,#2d5fa8);" role="img" aria-label="Photo of blue solar panels under a clear sky"></div>
    <p>Lorem ipsum dolor sit amet, consectetur adipiscing elit.</p>
  </article>
</section>

<!-- Testimonials -->
<section>
  <blockquote class="abs quote" style="top:4330px;left:146px;">I'm so grateful for this gym. The trainers are incredible, always pushing me to new limits. The state-of-the-art facilities and diverse classes keep me motivated. It's a community that feels like family.</blockquote>
  <div class="abs person" style="top:4478px;left:146px;">
    <div class="avatar" role="img" aria-label="Portrait photo of Alex"></div>
    <div><div class="person-name">ALEX</div><div class="person-role">Member</div></div>
  </div>
  <blockquote class="abs quote" style="top:4330px;left:668px;">I'm so grateful for this gym. The trainers are incredible, always pushing me to new limits. The state-of-the-art facilities and diverse classes keep me motivated. It's a community that feels like family.</blockquote>
  <div class="abs person" style="top:4478px;left:668px;">
    <div class="avatar" role="img" aria-label="Portrait photo of Lisa"></div>
    <div><div class="person-name">LISA</div><div class="person-role">Member</div></div>
  </div>
  <div class="abs dots" style="top:4644px;left:544px;"><span></span><span class="active"></span><span></span></div>
</section>

<!-- Footer -->
<footer class="abs site-footer">
  <div class="abs brand" style="top:60px;left:52px;color:#fff;"><span class="dot"></span>BrightVX</div>
  <p class="abs" style="top:136px;left:52px;width:330px;font-size:11px;line-height:14px;color:#ddd;">Lorem ipsum dolor sit amet, consectetur adipiscing elit, sed do eiusmod temporincididunt ut labore et doloremagna aliqua.</p>
  <div class="abs social" style="top:196px;left:56px;"><span></span><span></span><span></span></div>

  <h3 class="abs footer-heading" style="top:90px;left:430px;">QUICK LINKS</h3>
  <ul class="abs footer-list" style="top:126px;left:430px;">
    <li><svg width="18" height="18" viewBox="0 0 18 18" fill="none" stroke="#5ccf25" stroke-width="2"><path d="M5 4a7 7 0 1 0 8 0M9 1v8"/></svg>Home</li>
    <li><svg width="18" height="18" viewBox="0 0 18 18" fill="none" stroke="#5ccf25" stroke-width="2"><path d="M5 4a7 7 0 1 0 8 0M9 1v8"/></svg>About</li>
    <li><svg width="18" height="18" viewBox="0 0 18 18" fill="none" stroke="#5ccf25" stroke-width="2"><path d="M5 4a7 7 0 1 0 8 0M9 1v8"/></svg>Products</li>
    <li><svg width="18" height="18" viewBox="0 0 18 18" fill="none" stroke="#5ccf25" stroke-width="2"><path d="M5 4a7 7 0 1 0 8 0M9 1v8"/></svg>Prices</li>
  </ul>

  <h3 class="abs footer-heading" style="top:90px;left:658px;">OPENING HOURS</h3>
  <ul class="abs footer-list hours" style="top:126px;left:658px;">
    <li><svg width="20" height="20" viewBox="0 0 20 20" fill="none" stroke="#5ccf25" stroke-width="1.8"><circle cx="10" cy="10" r="8"/><path d="M10 5v5l3 2"/></svg>Mon - Fri 7am - 5pm</li>
    <li><svg width="20" height="20" viewBox="0 0 20 20" fill="none" stroke="#5ccf25" stroke-width="1.8"><circle cx="10" cy="10" r="8"/><path d="M10 5v5l3 2"/></svg>Saturday - Closed</li>
    <li><svg width="20" height="20" viewBox="0 0 20 20" fill="none" stroke="#5ccf25" stroke-width="1.8"><circle cx="10" cy="10" r="8"/><path d="M10 5v5l3 2"/></svg>Sunday - Closed</li>
  </ul>

  <h3 class="abs footer-heading" style="top:90px;left:958px;">STAY UPDATED</h3>
  <div class="abs email-field" style="top:134px;left:958px;">EMAIL ADDRESS</div>
  <a class="abs btn" style="top:186px;left:958px;width:180px;height:36px;background:var(--green);font-size:13px;font-weight:600;border-radius:0;" href="#">SIGNUP NOW</a>

  <div class="abs legal" style="top:398px;left:48px;">Copyright 2024 BrightVX. All Rights Reserved.</div>
  <div class="abs legal" style="top:398px;left:930px;">Privacy Policy | Terms &amp; Conditions</div>
</footer>

</body>
</html>
```